Basisdesign Buch-/E-Book-Cover für Lindqvist-Krimis
Sehr gute Zusammenarbeit! Soraya setzt sich ernsthaft mit dem Briefing auseinander, reagiert prompt und konstruktiv auf Änderungswünsche, kommuniziert kompetent und hilfsbereit. Äußerst empfehlenswert.
Zielgruppe
Ich schreibe Krimis, Thriller, Kriminalstories, Krimiparodien.
Meine Zielgruppe sind deutschsprachige Krimi-Leser.
Aufgabenstellung
Ich benötige ein Basisdesign für Buchcover (Höhe 2.343, Breite 1.518 Pixel – Print Forge, eBooks). Alle Bücher haben mit Crime zu tun, aber in verschiedenen Unter-Genres: Klassischer Kriminalroman, Thriller, Fantasy Thriller, Kurzgeschichten, Krimi-Parodien.
Ich benötige, quasi als Marke, dafür ein gleichbleibendes grafisches Element, z. B. einen Sockel im unteren Coverbereich, der den Autorennamen „Tobias Lindqvist“ und das jeweilige Unter-Genre enthält. Unter-Genres sind: Krimi, Thriller, Fantasy-Thriller, Kurzgeschichten und Krimi-Parodie. Das alles sollte auch noch im Format der Bücherhafen-Bücherlisten wie „Kunden kauften auch“ halbwegs lesbar sein.
Ein bisschen mörderisch und blutig sind alle Varianten.
Nachdem die Bandbreite vom Thriller bis zur Parodie reicht, sollte der gleichbleibende Markenbereich eine entsprechende grafische Bandbreite aufweisen, dabei aber die Grundmelodie Crime nicht aus den Augen verlieren.
Im oberen Bereich stelle ich mir Grafiken oder Hintergrundfotos vor, die für jedes Buch individuell gestaltet werden müssten, was jedoch über das Basisdesign hinausgeht. Die Wahl der Schriftart für Titel (bislang 11 – 25 Zeichen inkl. Leerzeichen) und allfällige Untertitel (im Umfang von maximal 30 Zeichen), sollte zu denen im Sockel passen.

```html
<!DOCTYPE html>
<html lang="de">
<head>
<meta charset="utf-8">
<title>Lindqvist-Krimis – Basisdesign Cover</title>
<link rel="stylesheet" href="https://fonts.googleapis.com/css2?family=Bebas+Neue&family=Open+Sans:wght@700&display=swap">
<style>
  :root {
    --page: #ffffff;
    --cover-black: #03040b;
    --sky-light: #e9dbd6;
    --sky-mid: #8a8fa8;
    --dusk-blue: #2a3558;
    --night: #070913;
    --badge: #0f1d36;
    --badge-text: #ffffff;
    --name-cream: #fbf7d8;
    --genre-ink: #111111;
    --title-light: #c9d0e0;
    --title-dark: #1d2748;
  }
  html, body {
    margin: 0;
    padding: 0;
    width: 848px;
    height: 1200px;
    overflow: hidden;
    background: var(--page);
  }
  .cover {
    position: absolute;
    left: 210px;
    top: 292px;
    width: 402px;
    height: 630px;
    background: var(--cover-black);
    overflow: hidden;
  }
  .cover-photo {
    position: absolute;
    inset: 0 0 auto 0;
    height: 360px;
    background: linear-gradient(180deg,
      var(--sky-light) 0%,
      #c9bfc4 22%,
      var(--sky-mid) 40%,
      var(--dusk-blue) 62%,
      var(--night) 85%,
      var(--cover-black) 100%);
  }
  .book-title {
    position: absolute;
    left: 0;
    right: 0;
    top: 190px;
    margin: 0;
    text-align: center;
    font-family: "Bebas Neue", sans-serif;
    font-weight: 400;
    font-size: 156px;
    line-height: 1;
    letter-spacing: 0.1em;
    padding-left: 0.1em;
    background: linear-gradient(180deg, var(--title-dark) 0%, var(--title-light) 35%, var(--dusk-blue) 70%, var(--title-dark) 100%);
    -webkit-background-clip: text;
    background-clip: text;
    color: transparent;
    -webkit-text-stroke: 1px rgba(110, 120, 150, 0.6);
  }
  .badge {
    position: absolute;
    left: -3px;
    top: 386px;
    width: 114px;
    height: 128px;
    border-radius: 50%;
    background: var(--badge);
    color: var(--badge-text);
    font-family: "Open Sans", sans-serif;
    font-weight: 700;
    text-align: center;
    display: flex;
    flex-direction: column;
    justify-content: center;
    line-height: 1.12;
  }
  .badge-small { font-size: 14px; }
  .badge-large { font-size: 19px; }
  .badge-dots { font-size: 10px; letter-spacing: 1px; margin-left: 50px; margin-top: 4px; }
  .brand-plinth {
    position: absolute;
    left: 0;
    right: 0;
    top: 496px;
    text-align: center;
    font-family: "Bebas Neue", sans-serif;
    color: var(--name-cream);
  }
  .author-first {
    display: block;
    font-size: 66px;
    line-height: 0.86;
  }
  .author-last-wrap {
    position: relative;
    display: inline-block;
  }
  .author-last {
    display: block;
    font-size: 78px;
    line-height: 0.9;
  }
  .genre {
    position: absolute;
    right: 0;
    top: 6px;
    padding: 1px 2px 0 5px;
    background: var(--name-cream);
    font-family: "Bebas Neue", sans-serif;
    font-size: 17px;
    line-height: 1;
    letter-spacing: 0.3em;
    color: var(--genre-ink);
  }
</style>
</head>
<body>
  <div class="cover">
    <div class="cover-photo" role="img" aria-label="Hintergrundfoto: Stacheldraht vor unscharfem Winterwald in Abenddämmerung, ein roter Blutstropfen hängt an einem Dorn"></div>
    <h1 class="book-title">Titel</h1>
    <div class="badge">
      <span class="badge-small">KUNDEN</span>
      <span class="badge-large">KAUFTEN</span>
      <span class="badge-small">AUCH</span>
      <span class="badge-dots">....</span>
    </div>
    <div class="brand-plinth">
      <span class="author-first">Tobias</span>
      <span class="author-last-wrap">
        <span class="author-last">Lindqvist</span>
        <span class="genre">Krimi</span>
      </span>
    </div>
  </div>
</body>
</html>
```